Ferris Contracting LLC Business Card Design

I am looking for a creative and unique business card design. We are a commercial construction general contractor. With the name "FERRIS" Contracting, I am hoping to see some neat designs that correlate with the name.

```html
<!DOCTYPE html>
<html lang="en">
<head>
<meta charset="utf-8">
<title>Ferris Contracting LLC – Business Card</title>
<link rel="stylesheet" href="https://fonts.googleapis.com/css2?family=Montserrat:wght@400;500;700;800&display=swap">
<style>
  :root {
    --bg: #2a2b2d;
    --card-black: #141516;
    --card-black-hi: #26282a;
    --blue: #2ea3e3;
    --blue-deep: #1d82c8;
    --silver: #b9bcc0;
    --white: #ffffff;
  }
  * { margin: 0; padding: 0; box-sizing: border-box; }
  html, body {
    width: 1200px; height: 874px; overflow: hidden;
    background: var(--bg);
    font-family: "Montserrat", sans-serif;
  }
  .canvas {
    width: 1200px; height: 874px;
    display: flex; flex-direction: column;
    align-items: center; justify-content: center; gap: 40px;
  }
  .card {
    position: relative;
    width: 640px; height: 366px;
    border-radius: 22px;
    overflow: hidden;
    box-shadow: 0 14px 30px rgba(0,0,0,.45);
  }
  .card-front {
    background: linear-gradient(135deg, var(--card-black-hi) 0%, var(--card-black) 55%, #0d0e0f 100%);
    display: flex; align-items: center; justify-content: center;
  }
  .brand {
    display: flex; align-items: center; gap: 16px;
    color: var(--blue);
    font-weight: 800;
  }
  .brand-dot {
    width: 22px; height: 22px; border-radius: 50%;
    background: var(--blue);
  }
  .brand-name { display: flex; flex-direction: column; line-height: 1; }
  .brand-name .word-main { font-size: 76px; letter-spacing: 1px; }
  .brand-name .word-sub { font-size: 20px; letter-spacing: 9px; margin-top: 8px; }

  .card-back .backdrop { position: absolute; inset: 0; }
  .card-back .brand {
    position: absolute; left: 390px; top: 120px;
    gap: 12px;
  }
  .card-back .brand-dot { width: 16px; height: 16px; }
  .card-back .brand-name .word-main { font-size: 56px; }
  .card-back .brand-name .word-sub { font-size: 15px; letter-spacing: 6px; margin-top: 6px; }

  .contact {
    position: absolute; left: 44px; top: 92px;
    color: var(--white);
  }
  .contact .person { font-size: 27px; font-weight: 700; letter-spacing: .5px; }
  .contact .role { font-size: 16px; font-weight: 400; margin-top: 2px; }
  .contact .address { font-size: 17px; line-height: 1.45; margin-top: 20px; }
  .contact .lines { list-style: none; margin-top: 18px; font-size: 17px; line-height: 1.55; }
  .contact .lines li { display: flex; align-items: center; gap: 8px; }
  .contact .lines svg { width: 13px; height: 13px; fill: var(--white); flex: none; }
</style>
</head>
<body>
<main class="canvas">

  <section class="card card-front">
    <div class="brand">
      <span class="brand-dot"></span>
      <div class="brand-name">
        <span class="word-main">FERRIS</span>
        <span class="word-sub">CONTRACTING</span>
      </div>
    </div>
  </section>

  <section class="card card-back">
    <svg class="backdrop" viewBox="0 0 640 366" preserveAspectRatio="none">
      <defs>
        <linearGradient id="blueFill" x1="0" y1="0" x2="0" y2="1">
          <stop offset="0" stop-color="#2ea3e3"/>
          <stop offset=".55" stop-color="#1d82c8"/>
          <stop offset="1" stop-color="#34ace6"/>
        </linearGradient>
        <linearGradient id="blackFill" x1="0" y1="0" x2="1" y2="1">
          <stop offset="0" stop-color="#1c1d1f"/>
          <stop offset="1" stop-color="#0f1011"/>
        </linearGradient>
      </defs>
      <rect width="640" height="366" fill="url(#blueFill)"/>
      <path d="M318,0 C300,170 410,300 640,318 L640,0 Z" fill="#9fa3a8"/>
      <path d="M334,0 C318,160 420,290 640,306 L640,0 Z" fill="url(#blackFill)"/>
    </svg>

    <div class="contact">
      <p class="person">LENA MARKOV</p>
      <p class="role">Managing Director</p>
      <p class="address">Your address, City<br>State, Zip 1200</p>
      <ul class="lines">
        <li><svg viewBox="0 0 24 24"><path d="M6.6 10.8a15.1 15.1 0 0 0 6.6 6.6l2.2-2.2a1 1 0 0 1 1-.25 11.4 11.4 0 0 0 3.6.57 1 1 0 0 1 1 1V20a1 1 0 0 1-1 1A17 17 0 0 1 3 4a1 1 0 0 1 1-1h3.5a1 1 0 0 1 1 1c0 1.25.2 2.45.57 3.57a1 1 0 0 1-.25 1z"/></svg>123 456 700</li>
        <li><svg viewBox="0 0 24 24"><path d="M2 5h20v14H2z M2 5l10 8 10-8" fill="none" stroke="#fff" stroke-width="2.4"/></svg>info@ferriscontracting.com</li>
        <li><svg viewBox="0 0 24 24"><circle cx="12" cy="12" r="10"/></svg>www.ferriscontracting.com</li>
      </ul>
    </div>

    <div class="brand">
      <span class="brand-dot"></span>
      <div class="brand-name">
        <span class="word-main">FERRIS</span>
        <span class="word-sub">CONTRACTING</span>
      </div>
    </div>
  </section>

</main>
</body>
</html>
```